Change an Existing THEME on a Shopify Site

We currently have a Shopify Site that we would like to launch soon. We picked a current theme [Tavel] and have made some basic changes to it but we don't really know what we're doing. We would like a new theme based on this one specifically built for our site. We already brand colours and a logo.

```html
<!DOCTYPE html>
<html lang="en">
<head>
<meta charset="utf-8">
<title>Pip Paws Home</title>
<link rel="stylesheet" href="https://fonts.googleapis.com/css2?family=Poppins:wght@400;500;600;700&display=swap">
<style>
:root{
  --teal:#9fd8d4;
  --teal-deep:#7fc9c3;
  --navy:#16204a;
  --orange:#f6ab4a;
  --corgi:#f3a955;
  --cream:#fdf1e3;
  --ink:#222;
  --white:#fff;
  --footer:#232323;
  --star:#f5c518;
}
*{margin:0;padding:0;box-sizing:border-box}
html,body{width:1200px;height:2500px;overflow:hidden;background:var(--white);font-family:'Poppins',sans-serif;color:var(--ink)}
.page{position:relative;width:1200px;height:2500px}
.abs{position:absolute}
.announce{left:0;top:0;width:1200px;height:52px;background:var(--teal);display:flex;align-items:center;justify-content:center;font-size:11.5px;font-weight:500;color:var(--navy)}
.nav{left:0;top:52px;width:1200px;height:76px;background:var(--white)}
.nav a{position:absolute;top:29px;font-size:12px;font-weight:500;color:var(--navy);text-decoration:none}
.nav a.active{color:#5aa9a2}
.logo-badge{left:522px;top:64px;width:156px;height:156px;border-radius:50%;background:var(--white);display:flex;align-items:center;justify-content:center;z-index:3}
.logo-badge .inner{width:132px;height:132px;border-radius:50%;background:var(--teal);display:flex;align-items:center;justify-content:center;text-align:center;font-weight:700;font-size:17px;line-height:1.15;color:var(--navy)}
.icons svg{position:absolute;top:78px}
.cart-count{left:976px;top:72px;width:15px;height:15px;border-radius:50%;background:var(--teal-deep);color:#fff;font-size:9px;display:flex;align-items:center;justify-content:center}
.hero{left:0;top:128px;width:1200px;height:530px;background:var(--teal)}
.hero h1{position:absolute;left:208px;top:104px;font-size:47px;line-height:55px;font-weight:700;color:var(--navy)}
.hero p{position:absolute;left:208px;top:242px;width:360px;font-size:15px;line-height:23px;font-weight:600;color:var(--navy)}
.btn{position:absolute;background:var(--orange);border-radius:30px;display:flex;align-items:center;justify-content:center;font-weight:600;color:var(--navy);box-shadow:0 6px 14px rgba(0,0,0,.12)}
.hero .btn{left:208px;top:320px;width:183px;height:56px;font-size:15px}
.ph{position:absolute}
.hero-photo{left:630px;top:0;width:570px;height:530px;background:linear-gradient(135deg,#c8dfe0 0%,#e6d7bf 38%,#d9c3a2 62%,#a9dcdc 100%)}
.mascot{background:linear-gradient(180deg,var(--corgi) 0%,var(--corgi) 42%,var(--cream) 43%,var(--cream) 100%);border-radius:46% 46% 22% 22%}
.deco{border-radius:18px}
.section-title{position:absolute;left:0;width:1200px;text-align:center;font-size:31px;font-weight:700;color:var(--navy)}
.collection{position:absolute;top:765px;width:244px;height:297px;border-radius:10px;background:var(--teal);overflow:hidden}
.collection .img{position:absolute;left:0;top:0;width:244px;height:240px}
.collection span{position:absolute;left:0;bottom:22px;width:100%;text-align:center;font-size:15px;font-weight:600;color:var(--navy)}
.arrivals{left:0;top:1216px;width:1200px;height:497px;background:var(--teal)}
.product{position:absolute;top:146px;width:183px}
.product .img{height:230px;background:var(--white);border-radius:10px;display:flex;align-items:center;justify-content:center}
.product .img div{width:80px;height:130px;border-radius:14px}
.product h3{margin-top:14px;text-align:center;font-size:15px;font-weight:600;color:var(--navy)}
.product .price{margin-top:4px;text-align:center;font-size:11px;color:var(--ink)}
.review{position:absolute;top:1849px;width:248px;height:283px;background:var(--white);border-radius:8px;box-shadow:0 4px 22px rgba(0,0,0,.07);text-align:center}
.review .stars{margin-top:30px;color:var(--star);font-size:14px;letter-spacing:1px}
.review q{display:block;margin:14px 22px 0;font-size:15px;line-height:22.5px;color:#333;quotes:"\201C" "\201D"}
.review .avatar{width:56px;height:56px;border-radius:50%;background:linear-gradient(#e2c6b4,#8d6b5a);margin:16px auto 0}
.review .name{margin-top:12px;font-size:11px;font-weight:600;color:var(--navy)}
.footer{left:0;top:2200px;width:1200px;height:300px;background:var(--footer);color:#fff}
.footer .brand{position:absolute;left:211px;top:64px;width:110px;height:110px;border-radius:50%;background:var(--teal);display:flex;align-items:center;justify-content:center;text-align:center;font-weight:700;font-size:15px;line-height:1.15;color:var(--navy)}
.footer h4{position:absolute;top:62px;font-size:15px;font-weight:600}
.footer ul{position:absolute;top:96px;list-style:none;font-size:12px;line-height:23px}
.footer .field{position:absolute;left:770px;top:99px;width:219px;height:46px;border:1px solid #ddd;font-size:9px;display:flex;align-items:center;padding-left:16px}
.footer .copy{position:absolute;left:208px;top:228px;font-size:11.5px}
.cards{position:absolute;left:703px;top:222px;display:flex;gap:9px}
.cards i{width:28px;height:18px;border-radius:3px;background:#e8e8e8}
</style>
</head>
<body>
<div class="page">
  <div class="abs announce">Free Shipping on Orders Over $50&nbsp;|&nbsp; Fun Finds for Happy Homes</div>

  <nav class="abs nav">
    <a class="active" style="left:208px">Home</a>
    <a style="left:285px">Shop</a>
    <a style="left:357px">About Us</a>
    <a style="left:451px">Contact</a>
  </nav>
  <div class="abs logo-badge"><div class="inner">Pip Paws<br>Home</div></div>
  <div class="icons">
    <svg style="left:892px" width="18" height="18" viewBox="0 0 18 18" fill="none" stroke="#16204a" stroke-width="1.5"><circle cx="7.5" cy="7.5" r="6"/><path d="M12 12l5 5"/></svg>
    <svg style="left:932px" width="18" height="18" viewBox="0 0 18 18" fill="none" stroke="#16204a" stroke-width="1.5"><circle cx="9" cy="5.5" r="4"/><path d="M2 17c0-4 3-6.5 7-6.5s7 2.5 7 6.5"/></svg>
    <svg style="left:965px" width="18" height="18" viewBox="0 0 18 18" fill="none" stroke="#16204a" stroke-width="1.5"><path d="M1 2h3l2 10h9l2-7H5"/><circle cx="7" cy="15.5" r="1.2"/><circle cx="14" cy="15.5" r="1.2"/></svg>
  </div>
  <div class="abs cart-count">1</div>

  <section class="abs hero">
    <div class="ph hero-photo" role="img" aria-label="Kitchen and kids products laid flat: brush, food containers, water bottle, wooden toys"></div>
    <div class="ph deco" role="img" aria-label="Paw prints and stars" style="left:6px;top:140px;width:170px;height:200px;background:linear-gradient(160deg,#c7e7e4,#f0c9d2)"></div>
    <h1>Home Joy,<br>Corgi-Approved</h1>
    <p>our charming collections bring joy to every corner of your home.</p>
    <div class="btn">Shop Now</div>
  </section>
  <div class="ph mascot" role="img" aria-label="Cartoon corgi sitting" style="left:4px;top:490px;width:168px;height:222px"></div>

  <h2 class="section-title" style="top:692px">Featured Collections</h2>
  <div class="collection" style="left:209px"><div class="img" role="img" aria-label="Baking tools: whisk, spatula, bowls" style="background:linear-gradient(135deg,#a9dcd6,#bfe8c8 50%,#f2b9cc)"></div><span>Cook and Bake</span></div>
  <div class="collection" style="left:478px"><div class="img" role="img" aria-label="Pantry shelf of storage containers" style="background:linear-gradient(180deg,#a9dcd6,#eadcc4 50%,#a9dcd6)"></div><span>Keep &amp; Store</span></div>
  <div class="collection" style="left:747px"><div class="img" role="img" aria-label="Kids bottle, teddy bear and toys" style="background:linear-gradient(135deg,#a9dcd6,#d8c2ad 50%,#bde0a8)"></div><span>Kids &amp; Toys</span></div>
  <div class="btn" style="left:537px;top:1104px;width:126px;height:46px;font-size:12px">View All</div>
  <div class="ph mascot" role="img" aria-label="Cartoon corgi with hearts and paw prints" style="left:1030px;top:990px;width:160px;height:226px"></div>

  <section class="abs arrivals">
    <h2 class="section-title" style="top:54px">New Arrivals</h2>
    <svg class="ph" style="left:180px;top:252px" width="14" height="22" viewBox="0 0 14 22" fill="none" stroke="#fff" stroke-width="2"><path d="M12 2L3 11l9 9"/></svg>
    <svg class="ph" style="left:1004px;top:252px" width="14" height="22" viewBox="0 0 14 22" fill="none" stroke="#fff" stroke-width="2"><path d="M2 2l9 9-9 9"/></svg>
    <div class="product" style="left:209px"><div class="img" role="img" aria-label="Stacked colourful bowls"><div style="background:linear-gradient(#f02d8c,#2a7fe0,#ff7a1a,#d6f01a)"></div></div><h3>Bake bowls set</h3><div class="price">$35.00</div></div>
    <div class="product" style="left:409px"><div class="img" role="img" aria-label="Stacked pastel bowls"><div style="background:linear-gradient(#1fb7a4,#ffe37a,#ff5f8f)"></div></div><h3>Bake bowls set 3</h3><div class="price">$35.00</div></div>
    <div class="product" style="left:609px"><div class="img" role="img" aria-label="Blue kids water bottle"><div style="width:40px;background:linear-gradient(#2d56c8,#1a2f8a)"></div></div><h3>Kids water bottle</h3><div class="price">$35.00</div></div>
    <div class="product" style="left:808px"><div class="img" role="img" aria-label="Purple lunch box"><div style="background:linear-gradient(#7b6ad8,#b3a2ef)"></div></div><h3>Lunch Box</h3><div class="price">$35.00</div></div>
    <div class="ph deco" role="img" aria-label="Paw prints and hearts" style="left:1080px;top:40px;width:112px;height:230px;background:linear-gradient(180deg,#b3cde0,#a7d4d6)"></div>
  </section>
  <div class="ph mascot" role="img" aria-label="Cartoon corgi wearing a chef hat" style="left:0;top:1450px;width:143px;height:263px;background:linear-gradient(180deg,#f4f6fb 0%,#f4f6fb 22%,var(--corgi) 23%,var(--corgi) 52%,#e8f0fa 53%,#e8f0fa 100%);border-radius:40% 40% 0 0"></div>

  <h2 class="section-title" style="top:1760px">Real Talk from Real Fans</h2>
  <div class="review" style="left:208px"><div class="stars">★★★★★</div><q>I didn't know Tidyware could be this cute! And the quality? Woof-level amazing.</q><div class="avatar" role="img" aria-label="Customer portrait"></div><div class="name">Nora P</div></div>
  <div class="review" style="left:476px"><div class="stars">★★★★★</div><q>My kids LOVED the bento lunchboxes. Durable and fun. Also... the corgi branding? Adorable.</q><div class="avatar" role="img" aria-label="Customer portrait"></div><div class="name">Leo K</div></div>
  <div class="review" style="left:744px"><div class="stars">★★★★★</div><q>Fast shipping, sweet packaging, and the Scratch &amp; Dent section had some real steals.</q><div class="avatar" role="img" aria-label="Customer portrait"></div><div class="name">Ivy T</div></div>
  <div class="ph" role="img" aria-label="Peeking cartoon corgi with teal paw prints" style="left:1040px;top:1810px;width:160px;height:190px;border-radius:50% 0 0 50%;background:linear-gradient(180deg,var(--corgi) 0%,var(--corgi) 45%,var(--cream) 46%,var(--cream) 100%)"></div>

  <footer class="abs footer">
    <div class="brand">Pip Paws<br>Home</div>
    <h4 style="left:414px">Quick links</h4>
    <ul style="left:412px"><li>Shop</li><li>About,</li><li>Contact</li></ul>
    <h4 style="left:574px">Info</h4>
    <ul style="left:575px"><li>Refund policy</li><li>Shipping policy</li><li>FAQ</li></ul>
    <h4 style="left:772px">Subscribe to our emails</h4>
    <div class="field">Enter your mail id
      <svg style="position:absolute;right:10px;top:14px" width="22" height="16" viewBox="0 0 22 16" fill="none" stroke="#fff" stroke-width="1.6"><path d="M1 8h19M13 1l7 7-7 7"/></svg>
    </div>
    <div class="copy">© 2025 © 2025, Pip Paws Home . Privacy policy&nbsp; Terms of service</div>
    <div class="cards"><i></i><i></i><i></i><i></i><i></i><i></i><i></i><i></i></div>
  </footer>
</div>
</body>
</html>
```